Halworth Builds, Carpentry Services

Business card for carpentry business in the Sunshine Coast.

Business card layout required using logo provided - provided both PDF copy and AI. Please let me know if you would like a the files for the logo symbol and text by itself.

Business Colours are grey, blue and white. The font colours codes for this design are Blue Hex # 00B4E6 and Hex # 39393B for the gray colour.

FYI font for logo is Gotham Bold.

Preference for a clean and striking layout that is simple and elegant.

Target Market(s)

Young Families, retirees, young couples requiring assistance with small to medium works/renovations on the Sunshine Coast.

Industry/Entity Type

Construction

Contact Information for Business Card

Dean Halworth
Carpenter
0481356027
dean@halworthbuilds.com.au
Kelvarra Bay, Coral Coast
RHLA Licensed Carpenter (In smaller font)

Font styles to use
Sans Serif

Colors

Designer to choose colors to be used in the design.

Requirements
Must have
• Logo provided must appear on the card, preferably on one side of the card by itself with the text on the alternate side
Nice to have
• Text on the other side of card, maybe grey background and white font here but happy for the designer to provide ideas here.
Should not have
• Use of other colours, other than the ones provided - white, grey and blue. Black optional.

```html
<!DOCTYPE html>
<html lang="en">
<head>
<meta charset="utf-8">
<title>Halworth Builds – Business Card</title>
<link rel="stylesheet" href="https://fonts.googleapis.com/css2?family=Montserrat:wght@500;700&family=Open+Sans:wght@400;600&display=swap">
<style>
  :root {
    --blue: #00b4e6;
    --grey: #39393b;
    --white: #ffffff;
    --page: #1c1c1d;
    --rule: rgba(255,255,255,0.8);
  }
  * { box-sizing: border-box; margin: 0; padding: 0; }
  html, body { width: 1200px; height: 1021px; overflow: hidden; }
  body {
    background: var(--page);
    font-family: "Open Sans", sans-serif;
    color: var(--white);
    position: relative;
  }
  .card {
    position: absolute;
    left: 220px;
    width: 760px;
    height: 434px;
    background: var(--grey);
    overflow: hidden;
    box-shadow: 0 12px 30px rgba(0,0,0,0.45);
  }
  .card--back { top: 48px; }
  .card--front { top: 530px; }

  .accent-band {
    position: absolute;
    top: 0;
    bottom: 0;
    width: 150px;
    background: var(--blue);
  }
  .card--back .accent-band { left: 0; }
  .card--front .accent-band { right: 0; }

  .brand {
    display: flex;
    align-items: center;
    gap: 14px;
  }
  .brand-mark {
    width: 18px;
    height: 18px;
    background: var(--blue);
    flex: none;
  }
  .brand-name {
    font-family: "Montserrat", sans-serif;
    font-weight: 700;
    color: var(--blue);
    text-transform: uppercase;
    letter-spacing: 0.04em;
    line-height: 1;
    white-space: nowrap;
  }
  .brand-tagline {
    font-family: "Montserrat", sans-serif;
    font-weight: 500;
    color: var(--white);
    text-transform: uppercase;
    letter-spacing: 0.38em;
    border-top: 1px solid var(--rule);
    border-bottom: 1px solid var(--rule);
    display: inline-block;
    white-space: nowrap;
  }

  .card--back .brand-block {
    position: absolute;
    left: 190px;
    right: 20px;
    top: 185px;
    text-align: center;
  }
  .card--back .brand-name { font-size: 38px; }
  .card--back .brand-tagline { font-size: 10px; margin-top: 14px; padding: 5px 6px 5px 10px; }

  .card--front .brand-block { position: absolute; left: 48px; top: 48px; }
  .card--front .brand-name { font-size: 28px; }
  .card--front .brand-tagline { font-size: 8px; margin-top: 10px; margin-left: 32px; padding: 4px 4px 4px 8px; }

  .person { position: absolute; left: 48px; top: 150px; }
  .person-name {
    font-family: "Montserrat", sans-serif;
    font-weight: 700;
    font-size: 24px;
    color: var(--blue);
  }
  .person-role { font-size: 17px; margin-top: 2px; }

  .contact {
    position: absolute;
    left: 48px;
    top: 236px;
    list-style: none;
    font-size: 18px;
    line-height: 1.55;
  }
  .contact li { display: flex; align-items: center; gap: 10px; white-space: nowrap; }
  .contact svg { width: 16px; height: 16px; flex: none; fill: none; stroke: var(--blue); stroke-width: 1.6; }
  .contact .address { padding-left: 26px; margin-bottom: 4px; }

  .licence {
    position: absolute;
    left: 48px;
    top: 378px;
    font-size: 15px;
    color: var(--blue);
  }
</style>
</head>
<body>

<section class="card card--back" aria-label="Card back">
  <div class="accent-band"></div>
  <div class="brand-block">
    <div class="brand-name">Halworth Builds</div>
    <div class="brand-tagline">Carpentry Services</div>
  </div>
</section>

<section class="card card--front" aria-label="Card front">
  <div class="accent-band"></div>

  <div class="brand-block">
    <div class="brand">
      <span class="brand-mark"></span>
      <span class="brand-name">Halworth Builds</span>
    </div>
    <div class="brand-tagline">Carpentry Services</div>
  </div>

  <div class="person">
    <div class="person-name">Dean Halworth</div>
    <div class="person-role">Carpenter</div>
  </div>

  <ul class="contact">
    <li class="address">Kelvarra Bay, Coral Coast</li>
    <li>
      <svg viewBox="0 0 16 16" aria-hidden="true"><path d="M4 1.5l2.5 3-1.5 2a9 9 0 0 0 4.5 4.5l2-1.5 3 2.5-1.5 2.5C7 14.5 1.5 9 1.5 3z"/></svg>
      0481356027
    </li>
    <li>
      <svg viewBox="0 0 16 16" aria-hidden="true"><rect x="1.5" y="3.5" width="13" height="9"/><path d="M1.5 3.5l6.5 5.5 6.5-5.5"/></svg>
      dean@halworthbuilds.com.au
    </li>
    <li>
      <svg viewBox="0 0 16 16" aria-hidden="true"><circle cx="8" cy="8" r="6.5"/><ellipse cx="8" cy="8" rx="3" ry="6.5"/><path d="M1.5 8h13"/></svg>
      www.halworthbuilds.com.au
    </li>
  </ul>

  <div class="licence">RHLA Licensed Carpenter</div>
</section>

</body>
</html>
```